Student project platform needs an awareness flyer

Tunvelo is a matchmaking and crowdfunding site for student projects. On this platform, students can team up with each other to invent a new product, innovate, or start a business. They can also raise funds for their project.

** I am in need of an 8x11" flyer to print and distribute digitally which notifies students of all different skill sets that this site exists.

The flyer should communicate that a diverse user base is being built on this site, with people who have skills in programming, engineering, design, business, finance, and so on.

The flyer should also be clean and modern, with an emphasis on creativity and innovation. I've attached the business' logo to give you an idea of the artistic style we have already established.

Target Market(s)

University students

Industry/Entity Type

Crowdfunding

Font styles to use
Serif
Sans Serif

Requirements
Must have
• * Clean and modern design
• * Color scheme of my logo: #336699 and #669933 (blue and green)
• * Convey that this site is for people of different skill sets: programming, engineering, design, business, finance, and so on.
• * See the attached "Tunvelo Copy.txt" for text to include on the flyer

```html
<!DOCTYPE html>
<html lang="en">
<head>
<meta charset="utf-8">
<title>Tunvelo – Student Project Flyer</title>
<link href="https://fonts.googleapis.com/css2?family=Oswald:wght@500;600&family=Montserrat:wght@300;400;700;800&family=Lato:wght@400;700&display=swap" rel="stylesheet">
<style>
  :root{
    --blue:#336699;
    --blue-deep:#1f4f8f;
    --blue-dark:#173e78;
    --green:#669933;
    --green-panel:#5e9438;
    --white:#ffffff;
    --ink:#1d2a1a;
    --page:#eeeeee;
  }
  *{box-sizing:border-box;margin:0;padding:0}
  html,body{width:1200px;height:1200px;overflow:hidden;background:var(--page)}
  .flyer{
    position:absolute;left:170px;top:45px;width:860px;height:1110px;
    background:var(--white);overflow:hidden;
    box-shadow:0 18px 40px rgba(0,0,0,.18);
    font-family:'Montserrat',sans-serif;
  }
  .artwork{position:absolute;left:0;top:0;width:860px;height:1110px}
  .brand{
    position:absolute;left:58px;top:432px;display:flex;align-items:center;gap:14px;
  }
  .brand-dot{width:52px;height:52px;border-radius:50%;background:var(--blue);flex:none}
  .brand-name{
    font-family:'Montserrat',sans-serif;font-weight:700;font-size:46px;
    letter-spacing:1px;color:var(--blue);line-height:1;
  }
  .join-badge{
    position:absolute;left:150px;top:560px;width:220px;height:220px;border-radius:50%;
    background:linear-gradient(160deg,#f4f4f4,#a9a9a9);
    display:flex;align-items:center;justify-content:center;
  }
  .join-badge-inner{
    width:184px;height:184px;border-radius:50%;
    background:radial-gradient(circle at 40% 30%,#3f7fc4,var(--blue-deep) 75%);
    display:flex;flex-direction:column;align-items:center;justify-content:center;color:var(--white);
  }
  .join-word{font-family:'Oswald',sans-serif;font-weight:600;font-size:62px;line-height:1}
  .join-name{font-family:'Montserrat',sans-serif;font-weight:800;font-size:28px;letter-spacing:1px;margin-top:4px}
  .headline{position:absolute;left:44px;top:812px;width:410px;line-height:1}
  .headline-small{font-family:'Oswald',sans-serif;font-weight:600;font-size:30px;color:var(--green);display:block}
  .headline-skills{font-family:'Oswald',sans-serif;font-weight:600;font-size:52px;color:var(--blue-deep);display:block;margin-top:2px}
  .headline-student{font-family:'Montserrat',sans-serif;font-weight:800;font-size:50px;color:var(--green);display:block;margin-top:-2px}
  .headline-projects{font-family:'Montserrat',sans-serif;font-weight:300;font-size:66px;color:var(--blue-deep);display:block;margin-top:0}
  .info{position:absolute;left:510px;top:520px;width:320px;color:var(--white)}
  .info-title{font-family:'Lato',sans-serif;font-weight:400;font-size:20px;letter-spacing:.5px}
  .info-title b{font-weight:700}
  .info-body{font-family:'Lato',sans-serif;font-size:13px;line-height:1.45;margin-top:10px}
  .call{font-family:'Montserrat',sans-serif;font-weight:700;font-size:19px;color:var(--ink);margin-top:40px;line-height:1.2}
  .goals{list-style:none;margin-top:34px}
  .goal{display:flex;align-items:flex-start;gap:18px;margin-bottom:26px}
  .goal-icon{width:34px;height:34px;border-radius:50%;background:var(--blue-deep);flex:none;display:flex;align-items:center;justify-content:center}
  .goal-text{flex:1;font-family:'Montserrat',sans-serif;font-size:22px;padding-bottom:10px;border-bottom:2px solid var(--white);line-height:1.1}
  .goal:last-child .goal-text{border-bottom:none}
  .site{
    position:absolute;right:70px;bottom:22px;color:var(--white);
    font-family:'Lato',sans-serif;font-size:17px;letter-spacing:4px;
  }
</style>
</head>
<body>
<main class="flyer">
  <svg class="artwork" viewBox="0 0 860 1110">
    <defs>
      <linearGradient id="photoTone" x1="0" y1="0" x2="1" y2="1">
        <stop offset="0" stop-color="#d9d2c8"/>
        <stop offset=".5" stop-color="#8c7566"/>
        <stop offset="1" stop-color="#4e4442"/>
      </linearGradient>
    </defs>
    <path d="M0 210 C140 150 240 170 300 210 L300 250 C200 220 90 250 0 310 Z" fill="var(--blue-deep)"/>
    <path d="M0 250 C120 200 220 210 300 250 L300 280 C200 250 100 280 0 340 Z" fill="var(--blue-dark)"/>
    <path role="img" aria-label="Photo of a diverse group of smiling university students standing together holding tablets and notebooks"
      d="M240 0 H860 V340 C720 350 600 380 540 450 C500 380 430 330 340 310 C280 295 250 260 240 210 Z" fill="url(#photoTone)"/>
    <path d="M230 220 C290 320 440 330 500 380 C560 430 470 500 330 580 C440 490 450 430 400 400 C330 360 250 320 230 220 Z" fill="var(--blue-deep)"/>
    <path d="M250 250 C320 330 430 345 470 380 C500 410 470 450 420 480 C450 440 440 410 400 390 C330 355 270 320 250 250 Z" fill="#4c86c6"/>
    <path d="M470 1040 V560 C520 470 650 420 860 390 V1040 Z" fill="var(--green-panel)"/>
    <path d="M470 560 C520 440 660 380 860 345 V395 C660 420 530 470 470 560 Z" fill="var(--blue-deep)"/>
    <path d="M0 1070 L470 1040 H860 V1110 H0 Z" fill="var(--blue-deep)"/>
  </svg>

  <div class="brand">
    <span class="brand-dot"></span>
    <span class="brand-name">TUNVELO</span>
  </div>

  <div class="join-badge">
    <div class="join-badge-inner">
      <span class="join-word">JOIN</span>
      <span class="join-name">TUNVELO</span>
    </div>
  </div>

  <h1 class="headline">
    <span class="headline-small">TO SUPPORT &amp;</span>
    <span class="headline-skills">LEND YOUR SKILLS</span>
    <span class="headline-student">to student</span>
    <span class="headline-projects">PROJECTS!</span>
  </h1>

  <section class="info">
    <h2 class="info-title">WHAT IS <b>TUNVELO?</b></h2>
    <p class="info-body">Tunvelo is a matchmaking and crowdfunding platform for student projects. It allows students to form teams of diverse skills and raise money to build, innovate, invent, or start a business.</p>
    <h3 class="call">CALLING ALL STUDENTS<br>WHO WANT TO</h3>
    <ul class="goals">
      <li class="goal">
        <span class="goal-icon"><svg width="18" height="18" viewBox="0 0 18 18"><rect x="2" y="10" width="3" height="6" fill="#fff"/><rect x="7.5" y="6" width="3" height="10" fill="#fff"/><rect x="13" y="3" width="3" height="13" fill="#fff"/></svg></span>
        <span class="goal-text">BUILD</span>
      </li>
      <li class="goal">
        <span class="goal-icon"><svg width="18" height="18" viewBox="0 0 18 18"><circle cx="9" cy="8" r="4.5" fill="#fff"/><rect x="7" y="13" width="4" height="3" fill="#fff"/></svg></span>
        <span class="goal-text">INNOVATE</span>
      </li>
      <li class="goal">
        <span class="goal-icon"><svg width="18" height="18" viewBox="0 0 18 18"><circle cx="9" cy="9" r="6" fill="none" stroke="#fff" stroke-width="2"/><circle cx="9" cy="9" r="2" fill="#fff"/></svg></span>
        <span class="goal-text">INVENT</span>
      </li>
      <li class="goal">
        <span class="goal-icon"><svg width="20" height="14" viewBox="0 0 20 14"><path d="M1 7 L6 3 L10 6 L14 3 L19 7 L12 12 L8 12 Z" fill="#fff"/></svg></span>
        <span class="goal-text">START<br>A BUSINESS</span>
      </li>
    </ul>
  </section>

  <p class="site">www.tunvelo.site</p>
</main>
</body>
</html>
```